Business Card Design Needed

Business car design required, logo will be supplied.

Brackenfield Heat Surveyors are looking to become the leading provider of energy performance certificates to estate agents, landlords and home owners in the Yorkshire region of the UK.

The business card must be double sided and professional looking. Estate agents receive hundreds of cards from contractors and our card must stand out.

I require a two sided business card that is clean, modern and created by a designer that can think outside of the box.

Brand colours can be supplied .

Please ask if you have any questions.

Target Market(s)

Estate agents, landlords and property owners

Industry/Entity Type

Property - estate agency - energy consultants

Contact Information for Business Card

Tomas Birchwell - Energy Assessor - 07351642170 - www.BrackenfieldHSV.co.uk - info@brackenfieldhsv.co.uk

Font styles to use
Serif
Sans Serif

Colors
00AB8E
00BBA5
67D7C9
C6EFE9
E9F9F6

Requirements
Must have
• Use the provided logo, clean, professional and stand out from the crowd
Nice to have
• Clever use of text, spacing and brand colours
Should not have
• Clip art

```html
<!DOCTYPE html>
<html lang="en">
<head>
<meta charset="utf-8">
<title>Brackenfield Heat Surveyors – Business Card</title>
<link href="https://fonts.googleapis.com/css2?family=Arimo:wght@400;700&display=swap" rel="stylesheet">
<style>
  :root {
    --page-bg: #e9e9e7;
    --card-blue: #0668a1;
    --card-blue-deep: #055a8c;
    --accent-lime: #a9c61c;
    --text-white: #ffffff;
    --rule-white: rgba(255,255,255,0.55);
  }
  * { box-sizing: border-box; margin: 0; padding: 0; }
  html, body { width: 1200px; height: 802px; overflow: hidden; }
  body {
    background: var(--page-bg);
    font-family: "Arimo", Arial, sans-serif;
    display: flex;
    align-items: center;
    justify-content: center;
    gap: 60px;
  }
  .card {
    position: relative;
    width: 525px;
    height: 300px;
    background: var(--card-blue);
    border-bottom: 5px solid var(--accent-lime);
    box-shadow: 0 10px 24px rgba(0,0,0,0.18);
    color: var(--text-white);
    overflow: hidden;
  }
  /* Front */
  .card-front { display: flex; align-items: center; padding: 0 36px; }
  .brand {
    display: flex;
    align-items: center;
    gap: 12px;
  }
  .brand-dot {
    width: 30px; height: 30px;
    border-radius: 50%;
    background: var(--accent-lime);
    flex: none;
  }
  .brand-name {
    font-size: 15px;
    font-weight: 400;
    line-height: 1.25;
    letter-spacing: 0.04em;
    text-transform: uppercase;
    color: var(--text-white);
    width: 130px;
  }
  .divider {
    width: 1px;
    align-self: stretch;
    margin: 92px 24px;
    background: var(--rule-white);
  }
  .contact { display: flex; flex-direction: column; }
  .person-name {
    font-size: 21px;
    font-weight: 700;
    color: var(--accent-lime);
    text-transform: uppercase;
    letter-spacing: 0.01em;
  }
  .person-role { font-size: 14px; margin-bottom: 14px; }
  .contact-list { list-style: none; font-size: 13px; line-height: 1.55; }
  .contact-list li { display: flex; align-items: center; gap: 8px; }
  .contact-list svg { width: 12px; height: 12px; fill: var(--accent-lime); flex: none; }
  /* Back */
  .card-back { display: flex; align-items: center; justify-content: flex-end; padding-right: 40px; }
  .card-back .divider-short {
    width: 1px; height: 58px;
    background: var(--rule-white);
    margin-right: 18px;
  }
  .card-back .brand-name {
    font-size: 24px;
    width: auto;
    letter-spacing: 0.03em;
    line-height: 1.2;
  }
</style>
</head>
<body>
  <section class="card card-front" aria-label="Business card front">
    <div class="brand">
      <span class="brand-dot"></span>
      <span class="brand-name">Brackenfield Heat Surveyors</span>
    </div>
    <span class="divider"></span>
    <div class="contact">
      <h1 class="person-name">Tomas Birchwell</h1>
      <p class="person-role">Energy Assessor</p>
      <ul class="contact-list">
        <li><svg viewBox="0 0 24 24"><path d="M6.6 10.8a15 15 0 0 0 6.6 6.6l2.2-2.2a1 1 0 0 1 1-.25 11.4 11.4 0 0 0 3.6.57 1 1 0 0 1 1 1V20a1 1 0 0 1-1 1A17 17 0 0 1 3 4a1 1 0 0 1 1-1h3.5a1 1 0 0 1 1 1c0 1.25.2 2.45.57 3.57a1 1 0 0 1-.25 1z"/></svg>07351642170</li>
        <li><svg viewBox="0 0 24 24"><path d="M2 5h20v14H2zm2 2v.5l8 5 8-5V7zm0 3v7h16v-7l-8 5z"/></svg>info@brackenfieldhsv.co.uk</li>
        <li><svg viewBox="0 0 24 24"><circle cx="12" cy="12" r="10"/></svg>www.BrackenfieldHSV.co.uk</li>
      </ul>
    </div>
  </section>

  <section class="card card-back" aria-label="Business card back">
    <span class="divider-short"></span>
    <span class="brand-name">Brackenfield<br>Heat Surveyors</span>
  </section>
</body>
</html>
```